Wedding Card Design Project

our wedding is on September 6th. we are looking for an elegant creative design for our wedding cards.

the card has to be BI-folded with and envelope, all of them has to have the design.

Name of the groom: Kareem
Name of the bride: Dina
date 6th of September 2013
venue : Bluewater Crest hotel

you have to give me  a design for the first page of the card. 

the page inside the card the borders and the writting. 
the envelope were the card will be placed where we will write the name of the guest invited. 

please use your imagination and colors. 

colors preferred: classy plus a little bit of yellow orange and lime green (bit essential )

Target Market(s)

these are friends from all ages from 17 to 60

Industry/Entity Type

Wedding

Requirements
Must have
• bi folder with an envelope.

```html
<!DOCTYPE html>
<html lang="en">
<head>
<meta charset="utf-8">
<title>Kareem and Dina – RSVP Card</title>
<link rel="stylesheet" href="https://fonts.googleapis.com/css2?family=Lobster&family=Oswald:wght@500;700&display=block">
<style>
  :root {
    --backdrop: #eeebe6;
    --card-white: #ffffff;
    --chevron-tone: #ececec;
    --band-grey: #a7a8aa;
    --band-shadow: #d4d5d6;
    --lime: #8cc63f;
    --yellow: #f2d21a;
    --yellow-deep: #c9a400;
    --ink-white: #ffffff;
    --ink-dark: #6d6e70;
    --ink-soft: #8a8b8d;
  }
  html, body {
    margin: 0;
    padding: 0;
    width: 1200px;
    height: 1000px;
    overflow: hidden;
    background: var(--backdrop);
  }
  .canvas { display: block; width: 1200px; height: 1000px; }
  .card-shadow { fill: rgba(0,0,0,0.12); }
  .chevron-field { fill: var(--chevron-tone); }
  .reply-panel { fill: var(--card-white); }
  .lime-stripe { fill: var(--lime); }
  .rsvp-title {
    font-family: "Oswald", sans-serif;
    font-weight: 700;
    font-size: 118px;
    fill: var(--yellow);
  }
  .event-detail {
    font-family: "Oswald", sans-serif;
    font-weight: 500;
    font-size: 21px;
    letter-spacing: 1px;
    fill: var(--ink-soft);
  }
  .name-band { fill: var(--band-grey); }
  .name-band-shadow { fill: var(--band-shadow); }
  .couple-name {
    font-family: "Lobster", cursive;
    font-size: 84px;
  }
  .couple-name.fill { fill: var(--yellow); }
  .couple-name.under { fill: var(--ink-white); }
  .couple-name.deep { fill: var(--yellow-deep); }
  .joiner {
    font-family: "Lobster", cursive;
    font-size: 30px;
  }
  .joiner.fill { fill: var(--ink-white); }
  .joiner.under { fill: var(--ink-dark); }
</style>
</head>
<body>
<svg class="canvas" viewBox="0 0 1200 1000" xmlns="http://www.w3.org/2000/svg">
  <rect class="card-shadow" x="403" y="110" width="400" height="812"/>
  <rect class="chevron-field" x="400" y="106" width="400" height="812" role="img" aria-label="Light grey chevron pattern covering the card"/>

  <g class="reply-side">
    <polygon class="reply-panel" points="400,216 708,132 708,296 400,362"/>
    <polygon class="lime-stripe" points="400,214 700,131 700,140 400,222"/>
    <g transform="translate(556,262) rotate(168)">
      <text class="event-detail" x="0" y="-10" text-anchor="middle">6TH OF SEPTEMBER 2013</text>
      <text class="event-detail" x="0" y="22" text-anchor="middle">BLUEWATER CREST HOTEL</text>
    </g>
    <text class="rsvp-title" text-anchor="middle" transform="translate(640,300) rotate(168)" y="0">RSVP</text>
  </g>

  <g class="names-side">
    <polygon class="name-band-shadow" points="452,850 800,760 800,770 466,856"/>
    <polygon class="name-band" points="452,630 800,560 800,760 452,850"/>
    <g transform="rotate(-11 625 700)">
      <text class="couple-name under" x="631" y="679" text-anchor="middle">Kareem</text>
      <text class="couple-name deep" x="628" y="676" text-anchor="middle">Kareem</text>
      <text class="couple-name fill" x="625" y="673" text-anchor="middle">Kareem</text>
      <text class="joiner under" x="626" y="712" text-anchor="middle">and</text>
      <text class="joiner fill" x="624" y="710" text-anchor="middle">and</text>
      <text class="couple-name under" x="621" y="779" text-anchor="middle">Dina</text>
      <text class="couple-name deep" x="618" y="776" text-anchor="middle">Dina</text>
      <text class="couple-name fill" x="615" y="773" text-anchor="middle">Dina</text>
    </g>
  </g>
</svg>
</body>
</html>
```